Property Developer - Simple yet Sophisticated and Sharp Business Card

We are a medium sized property developer involved mainly in townhouse developments and land subdivisions.

The company is looking for a simple, sharp and sophisticated business card that will be given to contractors, land owners, financiers etc and thus will need to look professional.

Property development related graphics and art can be used, however the card is not to be too "busy" or crowded. Our company name is KL Estates which could possibly be incorporated into the graphics or artwork.

Single sided and/or double sided designs will be acceptable.

A Simple, Sophisticated, Sharp design please!

Good Luck !

```html
<!DOCTYPE html>
<html lang="en">
<head>
<meta charset="utf-8">
<title>KL Estates – Business Card</title>
<link rel="stylesheet" href="https://fonts.googleapis.com/css2?family=Jost:wght@400;700&display=swap">
<style>
  :root {
    --page: #ffffff;
    --card: #050505;
    --ink-light: #ffffff;
    --ink-dark: #1a1a1a;
    --shadow: rgba(0, 0, 0, 0.55);
  }
  * { margin: 0; padding: 0; box-sizing: border-box; }
  html, body {
    width: 1200px;
    height: 920px;
    overflow: hidden;
    background: var(--page);
  }
  .canvas {
    position: relative;
    width: 1200px;
    height: 920px;
  }
  .business-card {
    position: absolute;
    left: 207px;
    top: 206px;
    width: 814px;
    height: 453px;
    background: var(--card);
    box-shadow: 6px 7px 7px var(--shadow);
    color: var(--ink-light);
    font-family: "Jost", "Futura", sans-serif;
    font-weight: 700;
  }
  .brand {
    position: absolute;
    left: 0;
    right: 0;
    top: 100px;
    display: flex;
    align-items: center;
    justify-content: center;
    gap: 22px;
  }
  .brand-circle {
    width: 46px;
    height: 46px;
    flex: none;
  }
  .brand-name {
    font-size: 70px;
    line-height: 1;
    letter-spacing: 4px;
    text-transform: uppercase;
    color: var(--ink-light);
  }
  .contact-list {
    position: absolute;
    left: 0;
    right: 0;
    top: 316px;
    list-style: none;
    text-align: center;
    font-size: 20px;
    line-height: 24.5px;
    letter-spacing: 0.4px;
  }
  .caption {
    position: absolute;
    left: 0;
    right: 0;
    top: 717px;
    text-align: center;
    font-family: "Jost", "Myriad Pro", sans-serif;
    font-weight: 400;
    font-size: 16px;
    color: var(--ink-dark);
  }
</style>
</head>
<body>
  <main class="canvas">
    <section class="business-card">
      <div class="brand">
        <svg class="brand-circle" viewBox="0 0 46 46" aria-hidden="true">
          <circle cx="23" cy="23" r="21" fill="none" stroke="#ffffff" stroke-width="2.5"/>
        </svg>
        <span class="brand-name">KL Estates</span>
      </div>
      <ul class="contact-list">
        <li>Phone: (07) 3200 4815</li>
        <li>Fax: (07) 3200 4816</li>
        <li>Email: projects@klestates-mail.com</li>
        <li>Postal: PO Box 2741 Riverview Heights QLD 4120</li>
      </ul>
    </section>
    <p class="caption">One sided card</p>
  </main>
</body>
</html>
```